tri-fold brochure design for psychology practice - all content provided

we are a psychology practice that specialises in diagnostic and educational assessments for children, adolescents and adults. We have an existing logo and I am attaching a word doc (tri-fold brochure) with the required content. I am also attaching our logo and other relevant content docs. The layout is only a sample and we are looking for someone to put this together into a consistent and better layout.

Target Market(s)

parents

Industry/Entity Type

education and health

Font styles to use
Other font styles liked:
• crimsonpro

Requirements
Must have
• our logo and the provided content

```html
<!DOCTYPE html>
<html lang="en">
<head>
<meta charset="utf-8">
<title>theleafroom – tri-fold brochure</title>
<link rel="stylesheet" href="https://fonts.googleapis.com/css2?family=Crimson+Pro:ital,wght@0,400;0,600;0,700;1,400&family=Roboto:wght@400;500&family=Montserrat:wght@800&family=Tinos:ital,wght@0,400;0,700;1,400&display=swap">
<style>
  :root{
    --backdrop:#5b5b5b;
    --paper:#f1f1f0;
    --green:#6fb03f;
    --green-bright:#8cc63f;
    --green-deep:#4d8f2a;
    --dark:#2b2f2a;
    --ink:#1e1e1e;
    --text:#2a2a2a;
    --white:#ffffff;
  }
  *{box-sizing:border-box;margin:0;padding:0}
  html,body{width:806px;height:1200px;overflow:hidden;background:var(--backdrop)}
  .brochure{position:absolute;left:23px;top:332px;width:760px;height:535px;background:var(--paper);box-shadow:0 10px 24px rgba(0,0,0,.45);overflow:hidden}
  .brochure-art{position:absolute;inset:0}
  .fold{position:absolute;top:0;bottom:0;width:1px;background:rgba(0,0,0,.08)}
  .fold--one{left:253px}.fold--two{left:507px}

  /* panel 1: process */
  .step{position:absolute;left:42px;width:169px;height:85px;background:var(--white);border-radius:4px;box-shadow:0 2px 4px rgba(0,0,0,.25);overflow:hidden}
  .step__title{height:20px;background:var(--green-bright);color:var(--white);font:500 11px/20px Roboto,sans-serif;text-align:center}
  .step__text{height:65px;padding:9px 10px 0;font:400 6.8px/1.32 Roboto,sans-serif;color:var(--text);text-align:center;background:linear-gradient(var(--white),#f0f0f0)}
  .step--understanding{top:178px}
  .step--identifying{top:300px}
  .step--guiding{top:420px}
  .step-arrow{position:absolute;left:112px;width:30px;height:22px}
  .step-arrow--one{top:272px}.step-arrow--two{top:394px}

  /* panel 2: testimonial + contact */
  .testimonial{position:absolute;left:278px;top:45px;width:203px;height:80px;border:1px solid var(--green);border-radius:5px;padding:15px 11px 0 12px}
  .testimonial__mark{position:absolute;font:700 24px/.8 Tinos,serif;color:var(--green-bright);background:var(--dark);padding:0 3px;height:16px;overflow:hidden}
  .testimonial__mark--open{left:8px;top:-9px}
  .testimonial__mark--close{right:8px;bottom:-9px}
  .testimonial__quote{font:italic 400 6.4px/1.38 Tinos,serif;color:#d9d9d9}
  .testimonial__author{position:absolute;right:34px;bottom:5px;font:700 6.8px/1 Tinos,serif;color:var(--white);font-style:normal}

  .brand{font-family:"Crimson Pro",serif;font-weight:600;color:var(--ink);letter-spacing:-.5px;white-space:nowrap}
  .brand-dot{display:inline-block;border-radius:50%;background:var(--green);vertical-align:middle}
  .brand-tagline{font:400 5.6px/1 Tinos,serif;color:#555;text-align:center}

  .contact{position:absolute;left:253px;width:254px;text-align:center}
  .contact__brand{top:338px}
  .contact__brand .brand{font-size:22px;line-height:1}
  .contact__brand .brand-dot{width:9px;height:9px;margin-right:5px}
  .contact__brand .brand-tagline{margin-top:3px;font-size:5px}
  .contact-pill{position:absolute;left:309px;top:393px;width:142px;height:20px;border-radius:10px;background:var(--green);color:var(--white);font:800 10px/20px Montserrat,sans-serif;letter-spacing:.3px;text-align:center}
  .contact__details{top:422px;font:400 9px/1.3 Tinos,serif;color:var(--text);font-style:normal}
  .contact__divider{display:flex;align-items:center;justify-content:center;gap:4px;margin-bottom:2px}
  .contact__divider span{display:block;width:30px;height:1px;background:var(--green)}
  .contact__line{display:flex;align-items:center;justify-content:center;gap:3px;margin-top:4px}
  .icon{width:7px;height:7px;flex:none}

  /* panel 3: cover */
  .cover{position:absolute;left:507px;width:253px;text-align:center}
  .cover__brand{top:84px}
  .cover__brand .brand{font-size:30px;line-height:1}
  .cover__brand .brand-dot{width:12px;height:12px;margin-right:6px}
  .cover__brand .brand-tagline{margin-top:4px;font-size:7.6px}
  .cover__headline{top:142px;font:700 27px/1.18 "Crimson Pro",serif;color:var(--green)}
  .web-pill{position:absolute;left:547px;top:489px;width:171px;height:19px;border-radius:10px;background:var(--green);color:var(--white);font:400 8.4px/19px Tinos,serif;letter-spacing:.6px;text-align:center}
</style>
</head>
<body>
<main class="brochure">
  <svg class="brochure-art" width="760" height="535" viewBox="0 0 760 535">
    <defs>
      <linearGradient id="officeTones" x1="0" y1="0" x2="1" y2="1">
        <stop offset="0" stop-color="#e9e6df"/><stop offset=".6" stop-color="#c9bba6"/><stop offset="1" stop-color="#8a7a66"/>
      </linearGradient>
      <linearGradient id="sessionTones" x1="0" y1="0" x2="1" y2="1">
        <stop offset="0" stop-color="#eef0f1"/><stop offset="1" stop-color="#c7c0b6"/>
      </linearGradient>
      <linearGradient id="familyTones" x1="0" y1="0" x2="1" y2="1">
        <stop offset="0" stop-color="#cfc3b3"/><stop offset=".5" stop-color="#efe7dc"/><stop offset="1" stop-color="#d9dcdf"/>
      </linearGradient>
    </defs>
    <g role="img" aria-label="Photo: a counsellor taking notes while a young man sits in a consultation room">
      <path d="M0 0H253V142C170 118 80 125 0 160Z" fill="url(#officeTones)"/>
    </g>
    <path d="M0 160C80 125 170 118 253 142V156C170 134 80 140 0 168Z" fill="var(--green)"/>
    <path d="M253 0H507V290C440 272 370 226 253 150Z" fill="var(--dark)"/>
    <path d="M253 150C370 226 440 272 507 290V304C430 290 360 248 253 164Z" fill="var(--green)"/>
    <path d="M507 290C600 262 690 252 760 272V292C690 276 600 286 507 304Z" fill="var(--green)"/>
    <g role="img" aria-label="Photo: a smiling mother with her young son in front of a small mirror">
      <path d="M507 304C600 286 690 276 760 292V535H507Z" fill="url(#familyTones)"/>
    </g>
    <circle cx="380" cy="221" r="74" fill="var(--white)"/>
    <g role="img" aria-label="Photo: a man talking with a therapist holding a clipboard">
      <circle cx="380" cy="221" r="70" fill="url(#sessionTones)"/>
    </g>
  </svg>
  <div class="fold fold--one"></div><div class="fold fold--two"></div>

  <section class="step step--understanding">
    <h2 class="step__title">Understanding</h2>
    <p class="step__text">Assessment starts with listening first, and then asking the right questions in order to ensure that we are understanding your concerns and hearing your questions.</p>
  </section>
  <svg class="step-arrow step-arrow--one" viewBox="0 0 30 22"><path d="M9 0H21V9H30L15 22L0 9H9Z" fill="var(--green-deep)"/></svg>
  <section class="step step--identifying">
    <h2 class="step__title">Identifying</h2>
    <p class="step__text">It is then our job to use our diagnostic and assessment knowledge and skills to collect the right data in order to address your concerns and provide answers to your questions.</p>
  </section>
  <svg class="step-arrow step-arrow--two" viewBox="0 0 30 22"><path d="M9 0H21V9H30L15 22L0 9H9Z" fill="var(--green-deep)"/></svg>
  <section class="step step--guiding">
    <h2 class="step__title">Guiding</h2>
    <p class="step__text">This then enables us to provide you with recommendations for accessing support and interventions that are based on current best practice and are suported by evidence.</p>
  </section>

  <blockquote class="testimonial">
    <span class="testimonial__mark testimonial__mark--open">“</span>
    <p class="testimonial__quote">My daughter hated school and wasn't learning to read like her classmates were. the team at theleafroom were able to diagnose her specific learning difficulty (reading disorder) and then worked with her and with me to help her to learn. I wish I had Claire as a teacher when I was a child - she is the perfect teacher!</p>
    <cite class="testimonial__author">Mia - Bayview</cite>
    <span class="testimonial__mark testimonial__mark--close">”</span>
  </blockquote>

  <div class="contact contact__brand">
    <div class="brand"><span class="brand-dot"></span>theleafroom</div>
    <p class="brand-tagline">diagnostic and educational assessments</p>
  </div>
  <div class="contact-pill">CONTACT US</div>
  <address class="contact contact__details">
    <div class="contact__divider"><span></span>
      <svg class="icon" viewBox="0 0 10 10"><path d="M5 0.5a3 3 0 0 1 3 3c0 2.2-3 5-3 5s-3-2.8-3-5a3 3 0 0 1 3-3z" fill="none" stroke="var(--green)" stroke-width="1"/><circle cx="5" cy="3.5" r="1" fill="var(--green)"/></svg>
    <span></span></div>
    <div>12/48 Harbour View Rd, Seacliff<br>NSW 2099</div>
    <div class="contact__line"><svg class="icon" viewBox="0 0 10 10"><circle cx="5" cy="5" r="4.3" fill="none" stroke="var(--green)"/><path d="M3.5 3l1 1-0.5.8c.4.8 1 1.3 1.7 1.7l.8-.5 1 1-.7.8C5.2 7.6 3 5.5 2.8 3.7z" fill="var(--green)"/></svg>02 8841 3076</div>
    <div class="contact__line"><svg class="icon" viewBox="0 0 10 10"><rect x="0.7" y="2" width="8.6" height="6" fill="none" stroke="var(--green)" stroke-width=".9"/><path d="M0.7 2L5 5.5L9.3 2" fill="none" stroke="var(--green)" stroke-width=".9"/></svg>info@theleafroom.com.au</div>
    <div class="contact__line"><svg class="icon" viewBox="0 0 10 10"><circle cx="5" cy="5" r="4.3" fill="none" stroke="var(--green)" stroke-width=".9"/><ellipse cx="5" cy="5" rx="1.8" ry="4.3" fill="none" stroke="var(--green)" stroke-width=".8"/><path d="M0.7 5H9.3" stroke="var(--green)" stroke-width=".8"/></svg>www.theleafroom.com.au</div>
  </address>

  <div class="cover cover__brand">
    <div class="brand"><span class="brand-dot"></span>theleafroom</div>
    <p class="brand-tagline">diagnostic and educational assessments</p>
  </div>
  <h1 class="cover cover__headline">Understanding<br>Identifying<br>Guiding</h1>
  <div class="web-pill">www.<b>theleafroom</b>.com.au</div>
</main>
</body>
</html>
```